Video Sharing Site

UPDATE 2: Thanks to everyone who has submitted so far. I have decided to include 2nd and 3rd prizes are well, and I believe with a robust price. If you chose to participate, I will be working with the 2nd and 3rd prize winners also to use your selected designs to complete the rest of the webpages as specified in the brief.

-

UPDATE 1: The key is attractive, SOPHISTICATED yet roomy.

You are free to use any software package you like ie. Joomla, Drupal, Wordpress etc. We just need access to the HTML/CSS.

-

Hello everyone.

We require the HTML/CSS for a video sharing website. Our website is called ClipHarborly.com. Think of a unique logo. However this is not the main focus. I will try to give you as much info about the website design as I can:

# Home page:
- with categories in sidebar
- video listings eg. popular, most viewed, etc.
- perhaps make promoted videos stand out

# simple login page

# User Profile page
- user details
- user uploaded videos
- profile comments

# User Profile Edit page

# User Profile Inbox page
- mock messages

# Search page
- list of videos that match search
- number of results
- pagination
- etc.

# Video page
- page where we are watching a video
- related videos
- video comments
- video description
- ratings (thumbs up/down)
- views
- tags
- etc.

# Video Categories page
- list of a few categories eg. newest, most viewed, highest rated, etc.
- with 10-15 videos under each

# Video Upload page with form

# About Us
- with subcategories in sidebar (different design to video categories in home page sidebar)

# Contact Us

# Header
- as any website an attractive search bar should accompany the header
- quick shortlinks to logged-in user eg. (5) comments, (3) inbox, logout, etc.

# Footer
- should be thick so that it can accommodate links to more specific (mock) web pages.

# General
- please be sure to include advertising
- Don't be afraid to use bold colors.
- I will not be selecting designs that are overly dark
- be sure that any page where video thumbnails are shown are accompanied by video rating, number of views and author.
- think about loading times as well. Avoid the use of large graphics where possible.

########### HINT ##########
The first two designs that I pick will be two different types:
- colorful
- quite conservative. Plenty of white with light greys
###########################

Thanks everybody who submits!

2nd and 3rd prized now included!

Just to keep you all updated. I have made a few changes to the brief. Mostly just to make it easier for you to gauge what I'm after.

I have received enough designs with blue in it. Please submit designs where blue is not a main color. Thank you all!

Industry/Entity Type

Software

Requirements
Must have
• A sophisticated layout. It must look like a professional video sharing website.

```html
<!DOCTYPE html>
<html lang="en">
<head>
<meta charset="utf-8">
<title>ClipHarborly.com – Inbox</title>
<link rel="stylesheet" href="https://fonts.googleapis.com/css2?family=Arimo:wght@400;700&family=Open+Sans:wght@300;400&display=swap">
<style>
:root{
  --orange:#f07a10;
  --orange-dark:#d85f00;
  --grey-text:#555;
  --grey-mid:#8c8c8c;
  --grey-light:#e9e9e9;
  --header-top:#ffffff;
  --header-bottom:#d9d9d9;
  --band:#eeeeee;
  --row-bg:#f3f3f3;
  --row-border:#dcdcdc;
  --bar-dark:#2e2e2e;
  --footer-top:#8a8a8a;
  --footer-bottom:#4a4a4a;
  --white:#ffffff;
}
*{box-sizing:border-box;margin:0;padding:0}
html,body{width:1200px;height:1056px;overflow:hidden;background:var(--white)}
body{font-family:"Arimo",Arial,sans-serif;color:var(--grey-text);font-size:14px}
.page{position:relative;width:1200px;height:1056px;overflow:hidden}
.abs{position:absolute}

/* header */
.site-header{position:absolute;left:0;top:0;width:1200px;height:168px;background:linear-gradient(var(--header-top),var(--header-bottom))}
.search-band{position:absolute;left:0;top:168px;width:1200px;height:41px;background:var(--band);border-bottom:1px solid #ddd}
.brand{left:66px;top:50px;font-family:"Open Sans",sans-serif;font-weight:300;font-size:43px;color:var(--orange);letter-spacing:-.5px}
.tagline{left:320px;top:45px;font-style:italic;font-weight:700;font-size:15px;color:#a9a9a9}
.user-bar{left:866px;top:19px;display:flex;align-items:center;gap:8px;font-size:16px;color:#444}
.user-bar .sep{color:#777}
.user-bar .count{font-size:21px;margin-right:6px}

.tab{top:139px;height:29px;display:flex;align-items:center;justify-content:center;font-size:15px;color:#222;background:linear-gradient(#fafafa,#d6d6d6);border-top:3px solid #c8c8c8}
.tab.is-active{background:linear-gradient(#bdbdbd,#8f8f8f);color:var(--white);border-top-color:#6e6e6e}
.nav-item{top:121px;height:47px;display:flex;align-items:center;justify-content:center;font-size:18px;color:#111;background:linear-gradient(#fdfdfd,#cfcfcf);border-top:4px solid #c4c4c4;box-shadow:0 0 3px rgba(0,0,0,.15)}
.nav-item.is-active{background:linear-gradient(#aaaaaa,#7d7d7d);color:var(--white);font-weight:700;border-top-color:#666}

.search-field{left:41px;top:176px;width:412px;height:25px;background:var(--white);border:1px solid #ddd}
.search-field svg{position:absolute;left:4px;top:3px}
.btn-orange{height:28px;display:flex;align-items:center;justify-content:center;font-size:15px;color:var(--white);background:linear-gradient(#ff9a3a,var(--orange-dark));border:1px solid #c9580a;border-radius:2px}

/* inbox title */
.page-title{left:18px;top:240px;display:flex;align-items:center;gap:7px;font-size:29px;color:var(--orange)}
.btn-grey{left:1047px;top:234px;width:126px;height:30px;display:flex;align-items:center;justify-content:center;font-size:14px;color:var(--white);background:linear-gradient(#c9c9c9,#8e8e8e);border:1px solid #8a8a8a;border-radius:2px}

.panel{left:26px;top:285px;width:1148px;height:521px;background:#fafafa;border:1px solid #e4e4e4;box-shadow:0 0 10px rgba(0,0,0,.12)}

.bar-head{height:39px;display:flex;align-items:center;color:var(--white);background:linear-gradient(#6a6a6a,var(--bar-dark) 60%,#4a4a4a);border-radius:3px 3px 0 0}
.side-menu{left:38px;top:292px;width:193px}
.side-menu .bar-head,.chat .bar-head{justify-content:center;font-size:21px;padding-right:30px}
.menu-list{list-style:none;background:var(--grey-light);height:295px;padding-top:15px}
.menu-list li{height:42px;display:flex;align-items:center;padding-left:20px;font-size:16px;color:#666}
.menu-list li::before{content:"";border-left:5px solid #555;border-top:4px solid transparent;border-bottom:4px solid transparent;margin-right:14px}

.chat{left:38px;top:631px;width:193px}
.chat-body{background:var(--grey-light);height:101px;padding-top:4px}
.chat-search{margin:0 3px;height:26px;background:var(--white);border:1px solid #ddd;font-size:15px;color:#444;display:flex;align-items:center;justify-content:center}
.chat-user{display:flex;align-items:center;gap:10px;padding:13px 0 0 9px;font-size:15px;color:#444}
.chat-user::before{content:"";width:11px;height:11px;border-radius:50%;background:var(--orange)}
.chat-status{display:flex;justify-content:space-between;padding:8px 13px 0 30px;font-size:12px;color:#888}

.inbox-table{left:234px;top:292px;width:931px}
.inbox-table .bar-head{font-size:15px;padding:0 12px 0 10px;gap:8px}
.check{width:15px;height:15px;background:var(--white);border:1px solid #ccc;flex:none}
.head-sort{margin-left:auto;display:flex;align-items:center;gap:10px}
.rows{list-style:none;margin-top:7px}
.row{position:relative;height:36px;margin-bottom:2.8px;background:var(--row-bg);border:1px solid var(--row-border);border-radius:4px;font-size:14px;color:#333}
.row .check{position:absolute;left:9px;top:9px;border-color:#ddd}
.row svg{position:absolute;left:32px;top:9px}
.row .name{position:absolute;left:57px;top:6px}
.row .title{position:absolute;left:210px;top:10px}
.row .date{position:absolute;right:15px;top:10px}

/* footer */
.site-footer{position:absolute;left:0;top:829px;width:1200px;height:227px;background:linear-gradient(var(--footer-top),var(--footer-bottom));color:var(--white)}
.foot-col{position:absolute;top:25px}
.foot-col h3{font-weight:400;font-size:16px;margin-bottom:18px}
.foot-col ul{list-style:none;padding-left:7px}
.foot-col li{font-size:12.5px;height:21.2px}
.follow{position:absolute;left:981px;top:155px;display:flex;align-items:center;gap:5px;font-size:14px}
.follow span.box{width:18px;height:18px;background:#d0d0d0;border-radius:2px}
.follow span.lbl{margin-right:5px}
</style>
</head>
<body>
<div class="page">

  <header class="site-header"></header>
  <div class="search-band"></div>

  <div class="abs brand">ClipHarborly.com</div>
  <div class="abs tagline">The Video Sharing Website</div>

  <div class="abs user-bar">
    <svg width="18" height="20" viewBox="0 0 18 20"><circle cx="9" cy="6" r="5" fill="#e8a06a"/><path d="M1 20c0-6 16-6 16 0z" fill="#3a78b8"/></svg>
    <span>User Name</span>
    <svg width="14" height="10" viewBox="0 0 14 10" style="margin-left:14px"><path d="M0 0h14L7 10z" fill="#777"/></svg>
    <span class="sep">|</span>
    <svg width="20" height="16" viewBox="0 0 20 16"><rect x="1" y="3" width="18" height="12" fill="#7ab648" stroke="#3f7a2a"/><path d="M1 3l9 7 9-7" fill="none" stroke="#fff"/></svg>
    <span class="count">0</span>
    <span class="sep">|</span>
    <svg width="20" height="20" viewBox="0 0 20 20"><circle cx="10" cy="10" r="8.5" fill="#fff" stroke="#f0a000" stroke-width="2.5"/><path d="M10 5v5h4" stroke="#d08000" stroke-width="2" fill="none"/></svg>
    <span>History</span>
  </div>

  <div class="abs tab is-active" style="left:42px;width:94px">Videos</div>
  <div class="abs tab" style="left:145px;width:95px">Categories</div>
  <div class="abs tab" style="left:249px;width:126px">Upload a Video</div>

  <nav>
    <div class="abs nav-item is-active" style="left:642px;width:93px">Home</div>
    <div class="abs nav-item" style="left:747px;width:94px">Recents</div>
    <div class="abs nav-item" style="left:852px;width:94px">Top Video</div>
    <div class="abs nav-item" style="left:958px;width:95px">Upload</div>
    <div class="abs nav-item" style="left:1065px;width:94px">Contact</div>
  </nav>

  <div class="abs search-field">
    <svg width="22" height="18" viewBox="0 0 22 18"><circle cx="7" cy="7" r="5" fill="none" stroke="#444" stroke-width="2"/><path d="M11 11l8 6" stroke="#444" stroke-width="3"/></svg>
  </div>
  <div class="abs btn-orange" style="left:465px;top:176px;width:117px">Video Search</div>
  <div class="abs btn-orange" style="left:1042px;top:176px;width:118px">Register Now</div>

  <h1 class="abs page-title" style="font-weight:400">
    <svg width="23" height="23" viewBox="0 0 23 23"><circle cx="11.5" cy="11.5" r="10" fill="none" stroke="#333" stroke-width="1.5"/><path d="M11.5 6v11M6 11.5h11" stroke="#333" stroke-width="2"/></svg>
    Inbox
  </h1>
  <div class="abs btn-grey">Account Settings</div>

  <div class="abs panel"></div>

  <aside class="abs side-menu">
    <div class="bar-head">Menu</div>
    <ul class="menu-list">
      <li>Inbox</li><li>Compose</li><li>Messages</li><li>Sent Items</li><li>Address Book</li><li>Video Responses</li>
    </ul>
  </aside>

  <aside class="abs chat">
    <div class="bar-head">Chat</div>
    <div class="chat-body">
      <div class="chat-search">Search, Add, or Invite</div>
      <div class="chat-user">User Name</div>
      <div class="chat-status"><span>Set your status here</span><svg width="9" height="6" viewBox="0 0 9 6"><path d="M0 0h9L4.5 6z" fill="#666"/></svg></div>
    </div>
  </aside>

  <section class="abs inbox-table">
    <div class="bar-head">
      <span class="check"></span>
      <svg width="10" height="7" viewBox="0 0 10 7"><path d="M0 0h10L5 7z" fill="#fff"/></svg>
      <span style="margin-left:4px">Name</span>
      <span style="margin-left:200px">Title</span>
      <span class="head-sort">Date | time
        <svg width="10" height="26" viewBox="0 0 10 26"><path d="M0 9L5 1l5 8zM0 17h10l-5 8z" fill="#fff"/></svg>
      </span>
    </div>
    <ul class="rows">
      <li class="row"><span class="check"></span><svg width="16" height="15" viewBox="0 0 16 15"><path d="M8 0l2.4 5 5.6.6-4.2 3.7 1.2 5.5L8 12l-5 2.8 1.2-5.5L0 5.6 5.6 5z" fill="#8a8a8a"/></svg><span class="name">Name</span><span class="title">Lorem Ipsum is simply dummy text of the printing</span><span class="date">Jun 22 2011 | 10.00 AM</span></li>
      <li class="row"><span class="check"></span><svg width="16" height="15" viewBox="0 0 16 15"><path d="M8 0l2.4 5 5.6.6-4.2 3.7 1.2 5.5L8 12l-5 2.8 1.2-5.5L0 5.6 5.6 5z" fill="#8a8a8a"/></svg><span class="name">Name</span><span class="title">Lorem Ipsum is simply dummy text of the printing</span><span class="date">Jun 22 2011 | 10.00 AM</span></li>
      <li class="row"><span class="check"></span><svg width="16" height="15" viewBox="0 0 16 15"><path d="M8 0l2.4 5 5.6.6-4.2 3.7 1.2 5.5L8 12l-5 2.8 1.2-5.5L0 5.6 5.6 5z" fill="#8a8a8a"/></svg><span class="name">Name</span><span class="title">Lorem Ipsum is simply dummy text of the printing</span><span class="date">Jun 22 2011 | 10.00 AM</span></li>
      <li class="row"><span class="check"></span><svg width="16" height="15" viewBox="0 0 16 15"><path d="M8 0l2.4 5 5.6.6-4.2 3.7 1.2 5.5L8 12l-5 2.8 1.2-5.5L0 5.6 5.6 5z" fill="#8a8a8a"/></svg><span class="name">Name</span><span class="title">Lorem Ipsum is simply dummy text of the printing</span><span class="date">Jun 22 2011 | 10.00 AM</span></li>
      <li class="row"><span class="check"></span><svg width="16" height="15" viewBox="0 0 16 15"><path d="M8 0l2.4 5 5.6.6-4.2 3.7 1.2 5.5L8 12l-5 2.8 1.2-5.5L0 5.6 5.6 5z" fill="#8a8a8a"/></svg><span class="name">Name</span><span class="title">Lorem Ipsum is simply dummy text of the printing</span><span class="date">Jun 22 2011 | 10.00 AM</span></li>
      <li class="row"><span class="check"></span><svg width="16" height="15" viewBox="0 0 16 15"><path d="M8 0l2.4 5 5.6.6-4.2 3.7 1.2 5.5L8 12l-5 2.8 1.2-5.5L0 5.6 5.6 5z" fill="#8a8a8a"/></svg><span class="name">Name</span><span class="title">Lorem Ipsum is simply dummy text of the printing</span><span class="date">Jun 22 2011 | 10.00 AM</span></li>
      <li class="row"><span class="check"></span><svg width="16" height="15" viewBox="0 0 16 15"><path d="M8 0l2.4 5 5.6.6-4.2 3.7 1.2 5.5L8 12l-5 2.8 1.2-5.5L0 5.6 5.6 5z" fill="#8a8a8a"/></svg><span class="name">Name</span><span class="title">Lorem Ipsum is simply dummy text of the printing</span><span class="date">Jun 22 2011 | 10.00 AM</span></li>
      <li class="row"><span class="check"></span><svg width="16" height="15" viewBox="0 0 16 15"><path d="M8 0l2.4 5 5.6.6-4.2 3.7 1.2 5.5L8 12l-5 2.8 1.2-5.5L0 5.6 5.6 5z" fill="#8a8a8a"/></svg><span class="name">Name</span><span class="title">Lorem Ipsum is simply dummy text of the printing</span><span class="date">Jun 22 2011 | 10.00 AM</span></li>
      <li class="row"><span class="check"></span><svg width="16" height="15" viewBox="0 0 16 15"><path d="M8 0l2.4 5 5.6.6-4.2 3.7 1.2 5.5L8 12l-5 2.8 1.2-5.5L0 5.6 5.6 5z" fill="#8a8a8a"/></svg><span class="name">Name</span><span class="title">Lorem Ipsum is simply dummy text of the printing</span><span class="date">Jun 22 2011 | 10.00 AM</span></li>
      <li class="row"><span class="check"></span><svg width="16" height="15" viewBox="0 0 16 15"><path d="M8 0l2.4 5 5.6.6-4.2 3.7 1.2 5.5L8 12l-5 2.8 1.2-5.5L0 5.6 5.6 5z" fill="#8a8a8a"/></svg><span class="name">Name</span><span class="title">Lorem Ipsum is simply dummy text of the printing</span><span class="date">Jun 22 2011 | 10.00 AM</span></li>
      <li class="row"><span class="check"></span><svg width="16" height="15" viewBox="0 0 16 15"><path d="M8 0l2.4 5 5.6.6-4.2 3.7 1.2 5.5L8 12l-5 2.8 1.2-5.5L0 5.6 5.6 5z" fill="#8a8a8a"/></svg><span class="name">Name</span><span class="title">Lorem Ipsum is simply dummy text of the printing</span><span class="date">Jun 22 2011 | 10.00 AM</span></li>
      <li class="row"><span class="check"></span><svg width="16" height="15" viewBox="0 0 16 15"><path d="M8 0l2.4 5 5.6.6-4.2 3.7 1.2 5.5L8 12l-5 2.8 1.2-5.5L0 5.6 5.6 5z" fill="#8a8a8a"/></svg><span class="name">Name</span><span class="title">Lorem Ipsum is simply dummy text of the printing</span><span class="date">Jun 22 2011 | 10.00 AM</span></li>
    </ul>
  </section>

  <footer class="site-footer">
    <div class="foot-col" style="left:129px"><h3>ClipHarborly</h3><ul><li>About</li><li>Press</li><li>Jobs</li><li>Blog</li><li>All Videos</li></ul></div>
    <div class="foot-col" style="left:319px"><h3>Participate</h3><ul><li>Advertise</li><li>Become a Motion Maker</li><li>Become an Official User</li><li>B2B Solution</li><li>ClipHarborly Publishers</li></ul></div>
    <div class="foot-col" style="left:567px"><h3>Help</h3><ul><li>Forums</li><li>FAQ</li><li>Contact</li><li>Family Filter On</li></ul></div>
    <div class="foot-col" style="left:756px"><h3>Legal Terms</h3><ul><li>Terms of Use</li><li>Privacy Policy</li><li>Prohibited Content</li><li>Copyright noticification</li><li>Child Protection</li></ul></div>
    <div class="foot-col" style="left:969px"><h3>Developers</h3><ul><li>Data API</li><li>Player API</li></ul></div>
    <div class="follow"><span class="lbl">Follow us on:</span><span class="box"></span><span class="box"></span><span class="box"></span></div>
  </footer>

</div>
</body>
</html>
```